Need Landing Page for Data Security Company

Need a new landing page (PSD) for our data security company (www.korvalim.com). We specialize in selling patented hard drive destruction machines that guarantee the data on your hard drives are unrecoverable. We have several large clients such as Trellio, Quibblr and Marquell just to name a few. Really want to have a landing page that sticks out.

Attached is a one pager we use just for emailing clients. We do not want the landing page to look like this. This is just for content to read. The landing page needs

Target Market(s)

Government, business corporations, IT decision makers. Not every day user

Industry/Entity Type

It Company

Number of Pages Required

1 page

Font styles to use
Other font styles liked:
• Match Current Website

Requirements
Must have
• Its a landing page so it needs a Contact us Section at the very top!!!
• Need to be a very attractive landing page.. Would like a mix of showcasing our products and also having some client list to show our bigger name clients (trellio, marquell, quibblr)
• Landing page needs to use the same color/style schema as current website. Also will be using the same menu structure as what exists today.
• www.korvalim.com
Nice to have
• Maybe some vidmora videos of our products?

```html
<!DOCTYPE html>
<html lang="en">
<head>
<meta charset="utf-8">
<title>Korvalim Technologies — Data Destruction Machines</title>
<link rel="stylesheet" href="https://fonts.googleapis.com/css2?family=Roboto:wght@300;400;500;700&family=Open+Sans:wght@400;600;700&display=swap">
<style>
:root{
  --green:#8cc63f;
  --ink:#222;
  --text:#666;
  --line:#e2e2e2;
  --black:#000;
  --footer:#141414;
  --footer-text:#aaa;
  --white:#fff;
}
*{box-sizing:border-box;margin:0;padding:0}
html,body{width:1200px;height:3492px;overflow:hidden}
body{font-family:"Open Sans",Arial,sans-serif;color:var(--text);background:var(--white);position:relative}
a{color:inherit;text-decoration:none}
ul{list-style:none}

/* Header */
.site-header{position:absolute;top:0;left:0;width:1200px;height:48px;background:rgba(10,10,10,.92);z-index:3}
.brand{position:absolute;left:90px;top:8px;display:flex;align-items:center;gap:8px;z-index:4}
.brand-dot{width:30px;height:30px;border-radius:50%;background:var(--green)}
.brand-name{font-family:"Roboto",sans-serif;font-weight:700;font-size:32px;color:var(--white);line-height:1}
.brand-tag{position:absolute;left:128px;top:44px;font-size:11px;color:#ddd;z-index:4;font-family:"Roboto",sans-serif}
.main-nav{position:absolute;right:96px;top:12px;display:flex;gap:6px}
.main-nav a{font-family:"Roboto",sans-serif;font-size:13px;color:#ddd;padding:4px 12px;border-radius:2px}
.main-nav a.active{background:var(--white);color:var(--ink)}

/* Hero with top contact strip */
.hero{position:absolute;top:0;left:0;width:1200px;height:540px;background:linear-gradient(160deg,#6d7d94 0%,#2e3a4e 45%,#10151f 100%)}
.top-contact{position:absolute;top:64px;left:90px;display:flex;gap:22px;align-items:center;font-size:12px;color:#e6e6e6;z-index:2}
.top-contact strong{font-family:"Roboto",sans-serif;font-weight:500;color:var(--green);font-size:13px}
.top-contact span{display:flex;align-items:center;gap:6px}
.hero-thumbs{position:absolute;top:474px;left:520px;display:flex;gap:8px;z-index:2}
.hero-thumbs div{width:112px;height:112px;border-radius:50%;border:4px solid var(--white);background:linear-gradient(135deg,#c9d2de,#5f7896)}
.clients{position:absolute;top:552px;left:890px;width:230px;text-align:right;font-size:12px;line-height:18px;color:var(--text)}
.clients strong{display:block;font-family:"Roboto",sans-serif;font-weight:500;color:var(--green);font-size:13px}

/* About */
.about{position:absolute;top:680px;left:120px;width:960px;height:340px}
.about-photo{position:absolute;left:0;top:0;width:480px;height:340px;background:linear-gradient(135deg,#f1f1f1,#bcc6d6 60%,#3c6fb8);border:1px solid var(--line)}
.about-body{position:absolute;left:520px;top:0;width:440px}
.section-title{font-family:"Roboto",sans-serif;font-weight:500;color:var(--green);font-size:24px;margin-bottom:14px}
.about-body p{font-size:13px;line-height:22px}
.btn{display:inline-block;background:var(--green);color:var(--white);font-size:12px;font-weight:600;padding:7px 20px;border-radius:14px;margin-top:24px}

.divider{position:absolute;top:1090px;left:80px;width:1040px;height:1px;background:var(--line)}

/* Products */
.products{position:absolute;top:1128px;left:80px;width:1040px}
.product-grid{display:grid;grid-template-columns:repeat(4,230px);column-gap:40px;row-gap:36px;margin-top:8px}
.product-shot{height:184px;background:linear-gradient(180deg,#e8e8e8,#bdbdbd);border:1px solid var(--line)}
.product-shot.featured{background:linear-gradient(180deg,var(--green),#a9d66b)}
.product-name{font-size:12px;color:var(--green);font-weight:600;margin:10px 0 6px}
.product-points li{font-size:11px;line-height:16px;padding-left:14px;position:relative;margin-bottom:6px}
.product-points li::before{content:"";position:absolute;left:2px;top:5px;border-left:6px solid var(--green);border-top:4px solid transparent;border-bottom:4px solid transparent}

/* Security features */
.features{position:absolute;top:1920px;left:0;width:1200px;height:770px;background:var(--black);color:#ccc}
.feature-core{position:absolute;left:450px;top:230px;width:300px;height:300px;border-radius:50%;background:radial-gradient(circle,#c7d4e6,#5c7fb2 55%,#1b2a44)}
.feature-icon{position:absolute;width:76px;height:76px;border-radius:50%;background:var(--white);border:5px solid var(--green);display:flex;align-items:center;justify-content:center}
.feature-text{position:absolute;width:270px;font-size:11px;line-height:15px}
.feature-text h3{font-family:"Roboto",sans-serif;font-size:14px;color:var(--white);font-weight:500;margin-bottom:4px}
.feature-text.center{text-align:center}
.feature-text.right{text-align:right}

/* Blog */
.blog{position:absolute;top:2740px;left:80px;width:1040px}
.post-grid{display:grid;grid-template-columns:500px 500px;column-gap:40px;row-gap:36px;margin-top:6px}
.post{display:flex;gap:16px}
.post-photo{width:184px;height:124px;flex:none;background:linear-gradient(135deg,#2f4f6f,#9cb3c9)}
.post-photo.alt{background:linear-gradient(135deg,#0e5f5a,#79b8a8)}
.post h3{font-family:"Roboto",sans-serif;font-size:15px;color:var(--green);font-weight:500;margin-bottom:6px}
.post p{font-size:11px;line-height:16px}
.post .more{display:block;font-size:11px;color:var(--green);margin-top:8px}

/* Footer */
.site-footer{position:absolute;top:3160px;left:0;width:1200px;height:332px;background:var(--footer);color:var(--footer-text)}
.footer-col{position:absolute;top:40px;font-size:12px;line-height:20px}
.footer-col h4{font-family:"Roboto",sans-serif;font-size:20px;color:var(--green);font-weight:500;margin-bottom:6px;padding-bottom:6px;border-bottom:1px solid #333;width:180px}
.contact-line{display:flex;align-items:center;gap:8px;margin-top:6px}
.social{display:flex;gap:10px;margin:6px 0 20px}
.social span{width:26px;height:26px;border-radius:50%;background:#555}
.footer-brand{font-family:"Roboto",sans-serif;font-weight:700;font-size:26px;color:var(--white);display:flex;align-items:center;gap:8px}
.footer-brand i{width:22px;height:22px;border-radius:50%;background:var(--green);display:block}
.copyright{position:absolute;bottom:12px;left:0;width:1200px;text-align:center;font-size:10px;color:#777;border-top:1px solid #2a2a2a;padding-top:10px}
</style>
</head>
<body>

<div class="hero" role="img" aria-label="Photograph of a padlock resting on a laptop keyboard"></div>
<header class="site-header">
  <nav class="main-nav">
    <a class="active" href="#">Home</a><a href="#">About us</a><a href="#">Products</a><a href="#">Services</a><a href="#">Downloads</a><a href="#">Map</a><a href="#">Contact Us</a>
  </nav>
</header>
<div class="brand"><span class="brand-dot"></span><span class="brand-name">Korvalim</span></div>
<div class="brand-tag">Enterprise Data Destruction</div>

<div class="top-contact">
  <strong>Contact us</strong>
  <span><svg width="12" height="12" viewBox="0 0 24 24"><path d="M6 2l4 4-2 3a12 12 0 007 7l3-2 4 4-3 4C10 21 3 14 2 5z" fill="#8cc63f"/></svg>+1 (555) 014-2290</span>
  <span><svg width="12" height="12" viewBox="0 0 24 24"><rect x="2" y="5" width="20" height="14" fill="#8cc63f"/><path d="M2 5l10 8 10-8" stroke="#222" stroke-width="2" fill="none"/></svg>hello@korvalim.com</span>
</div>

<div class="hero-thumbs">
  <div role="img" aria-label="Hard drive close-up"></div>
  <div role="img" aria-label="Server room"></div>
  <div role="img" aria-label="Padlock on circuit board"></div>
</div>
<div class="clients"><strong>Trusted by</strong>Trellio · Quibblr · Marquell</div>

<section class="about">
  <div class="about-photo" role="img" aria-label="Server with blue network cables plugged in"></div>
  <div class="about-body">
    <h2 class="section-title">About Korvalim Technologies</h2>
    <p>Our patented machines physically destroy hard drives so the data they held can never be read again. Government agencies, corporations and IT leaders rely on us to retire storage safely, quickly and with full audit trails. Every unit is engineered for daily use in secure rooms, runs quietly and leaves nothing behind but fragments. We support each client from first demonstration through installation and long-term service, with trained engineers on call and certified destruction reports for every drive processed.</p>
    <a class="btn" href="#">Read more</a>
  </div>
</section>

<div class="divider"></div>

<section class="products">
  <h2 class="section-title">Products</h2>
  <div class="product-grid">
    <article><div class="product-shot featured" role="img" aria-label="DiskBreaker 1000 desktop unit"></div><p class="product-name">DiskBreaker 1000</p><ul class="product-points"><li>Crushes hard drives in seconds with one button press.</li><li>Compact body fits under any office desk easily.</li></ul></article>
    <article><div class="product-shot" role="img" aria-label="DiskBreaker 2000 unit"></div><p class="product-name">DiskBreaker 2000</p><ul class="product-points"><li>Handles laptop and desktop drives in one slot.</li><li>Locked chamber keeps fragments safe until emptied.</li></ul></article>
    <article><div class="product-shot" role="img" aria-label="DiskBreaker 3000 unit"></div><p class="product-name">DiskBreaker 3000</p><ul class="product-points"><li>Built for data centres with heavy daily volume.</li><li>Logs every drive for complete audit reporting.</li></ul></article>
    <article><div class="product-shot" role="img" aria-label="DiskBreaker 3500 unit"></div><p class="product-name">DiskBreaker 3500</p><ul class="product-points"><li>Dual feed slots double throughput on busy days.</li><li>Quiet motor suits shared office environments.</li></ul></article>
    <article><div class="product-shot" role="img" aria-label="DiskBreaker Compact unit"></div><p class="product-name">DiskBreaker Compact</p><ul class="product-points"><li>Portable design for field and branch offices.</li><li>Runs from standard wall power anywhere.</li></ul></article>
    <article><div class="product-shot" role="img" aria-label="DiskBreaker SSD unit"></div><p class="product-name">DiskBreaker SSD 500</p><ul class="product-points"><li>Shreds solid state drives into tiny pieces.</li><li>Meets strict government disposal standards.</li></ul></article>
    <article><div class="product-shot" role="img" aria-label="TapeBreaker unit"></div><p class="product-name">TapeBreaker 200</p><ul class="product-points"><li>Destroys backup tapes and optical media fully.</li><li>Sealed waste bin with simple removal tray.</li></ul></article>
    <article><div class="product-shot" role="img" aria-label="DiskBreaker Compact Plus unit"></div><p class="product-name">DiskBreaker Compact Plus</p><ul class="product-points"><li>Adds drive counter and printed receipts.</li><li>Steel housing rated for secure facilities.</li></ul></article>
  </div>
</section>

<section class="features">
  <div class="feature-core" role="img" aria-label="Hard drive platter with a padlock"></div>

  <div class="feature-text center" style="left:465px;top:40px"><h3>On-site Destruction</h3>Drives are destroyed on site, so sensitive data never leaves your building or your sight at any point.</div>
  <div class="feature-text right" style="left:110px;top:220px"><h3>Full Audit Trail</h3>Each machine records serial numbers and times, giving auditors a clear trail of every drive destroyed.</div>
  <div class="feature-text right" style="left:110px;top:400px"><h3>Simple Controls</h3>Any trained staff member can run a destruction job in under a minute.</div>
  <div class="feature-text" style="left:830px;top:220px"><h3>Patented Crushing</h3>Patented crushing heads bend and fracture platters beyond any known recovery method.</div>
  <div class="feature-text" style="left:830px;top:400px"><h3>Sealed Chambers</h3>Sealed chambers contain fragments safely until they are collected for certified recycling.</div>
  <div class="feature-text center" style="left:465px;top:610px"><h3>Expert Support</h3>Our service team keeps every unit running with fast support and scheduled maintenance visits.</div>

  <div class="feature-icon" style="left:562px;top:150px"><svg width="34" height="34" viewBox="0 0 24 24"><path d="M12 2l8 3v6c0 5-3.5 9-8 11-4.5-2-8-6-8-11V5z" fill="#222"/></svg></div>
  <div class="feature-icon" style="left:394px;top:254px"><svg width="34" height="34" viewBox="0 0 24 24"><rect x="3" y="4" width="18" height="16" rx="2" fill="#222"/><circle cx="12" cy="12" r="4" fill="#fff"/></svg></div>
  <div class="feature-icon" style="left:394px;top:402px"><svg width="34" height="34" viewBox="0 0 24 24"><rect x="3" y="5" width="18" height="12" rx="1" fill="#222"/><rect x="9" y="18" width="6" height="2" fill="#222"/></svg></div>
  <div class="feature-icon" style="left:730px;top:254px"><svg width="34" height="34" viewBox="0 0 24 24"><rect x="2" y="8" width="14" height="8" rx="1" fill="#222"/><path d="M16 10l6-3v10l-6-3z" fill="#222"/></svg></div>
  <div class="feature-icon" style="left:730px;top:402px"><svg width="34" height="34" viewBox="0 0 24 24"><rect x="5" y="10" width="14" height="11" rx="1" fill="#222"/><path d="M8 10V7a4 4 0 018 0v3" stroke="#222" stroke-width="2" fill="none"/></svg></div>
  <div class="feature-icon" style="left:562px;top:500px"><svg width="34" height="34" viewBox="0 0 24 24"><path d="M4 16l6-6 4 4 6-8" stroke="#222" stroke-width="2.5" fill="none"/></svg></div>
</section>

<section class="blog">
  <h2 class="section-title">Blog</h2>
  <div class="post-grid">
    <article class="post"><div class="post-photo" role="img" aria-label="Laptop with padlock and cables"></div><div><h3>Perfect experience &amp; knowledge</h3><p>Why physical destruction remains the only certain way to retire old drives, and what auditors now expect from IT teams handling disposal.</p><a class="more" href="#">Read More</a></div></article>
    <article class="post"><div class="post-photo alt" role="img" aria-label="Circuit board close-up"></div><div><h3>Perfect experience &amp; knowledge</h3><p>A short guide to solid state storage and why wiping software alone cannot guarantee data is gone for good.</p><a class="more" href="#">Read More</a></div></article>
    <article class="post"><div class="post-photo" role="img" aria-label="Network cables in a server rack"></div><div><h3>Perfect experience &amp; knowledge</h3><p>How large organisations plan drive retirement schedules and keep records that satisfy regulators year after year.</p><a class="more" href="#">Read More</a></div></article>
    <article class="post"><div class="post-photo alt" role="img" aria-label="Open hard drive platters"></div><div><h3>Perfect experience &amp; knowledge</h3><p>Inside our newest machine: the design choices that make it faster, quieter and safer for everyday office use.</p><a class="more" href="#">Read More</a></div></article>
  </div>
</section>

<footer class="site-footer">
  <div class="footer-col" style="left:80px">
    <h4>Contact us</h4>
    <p>418 Harbour Lane, Suite 12<br>Westbrook, NY 10221</p>
    <p class="contact-line"><svg width="12" height="12" viewBox="0 0 24 24"><path d="M6 2l4 4-2 3a12 12 0 007 7l3-2 4 4-3 4C10 21 3 14 2 5z" fill="#8cc63f"/></svg>+1 (555) 014-2290</p>
    <p class="contact-line"><svg width="12" height="12" viewBox="0 0 24 24"><rect x="2" y="5" width="20" height="14" fill="#8cc63f"/><path d="M2 5l10 8 10-8" stroke="#141414" stroke-width="2" fill="none"/></svg>hello@korvalim.com</p>
  </div>
  <div class="footer-col" style="left:420px">
    <h4>Quick Links</h4>
    <ul><li>Home</li><li>About us</li><li>Our Clients</li><li>Services</li><li>Downloads</li><li>Contact Us</li></ul>
  </div>
  <div class="footer-col" style="left:688px">
    <h4>Products</h4>
    <ul><li>DiskBreaker 1000</li><li>DiskBreaker 2000</li><li>DiskBreaker 3000</li><li>DiskBreaker 3500</li><li>DiskBreaker Compact</li><li>DiskBreaker SSD 500</li><li>TapeBreaker 200</li></ul>
  </div>
  <div class="footer-col" style="left:960px">
    <h4>Social Medias</h4>
    <div class="social"><span aria-label="trellio"></span><span aria-label="quibblr"></span><span aria-label="marquell"></span><span aria-label="vidmora"></span></div>
    <div class="footer-brand"><i></i>Korvalim</div>
  </div>
  <p class="copyright">© 2024 www.korvalim.com | All rights reserved</p>
</footer>

</body>
</html>
```